Business Card Design Project

- makeup artist business card

- original and creative

- Elegant design

- Feel free to come out with cool designs but stick to being elegant and attractive

- Design relates to makeup

- includes name, occupation, contact numbers, email, website

- regular size business card

- round corner card

- double sided

- on 1 side it should just have the website name in the center " browsandblush.example "

Industry/Entity Type

Business

Requirements
Must have
• Marla Voss
Makeup Artist
USA: +1 (415)872-6410
Singapore: +65 83027715
marlavoss@browsandblush.example
www.browsandblush.example
Should not have
• nothing cartoon looking.
Pictures of makeup being grab from the internet.. Examples: eyes or lips.

```html
<!DOCTYPE html>
<html lang="en">
<head>
<meta charset="utf-8">
<title>Marla Voss — Makeup Artist Business Card</title>
<link rel="stylesheet" href="https://fonts.googleapis.com/css2?family=Noto+Sans:wght@400;600&display=swap">
<style>
  :root {
    --page: #ffffff;
    --blush: #f5b2bb;
    --peach: #f3cfb4;
    --butter: #f2ecb0;
    --ink: #86683f;
    --name: #8a6b3a;
    --panel: rgba(255, 250, 240, 0.28);
    --plume-light: #fffaf0;
    --plume-warm: #efe3c6;
    --web-light: #fbf6ee;
  }
  html, body {
    margin: 0;
    padding: 0;
    width: 1200px;
    height: 829px;
    overflow: hidden;
    background: var(--page);
  }
  .canvas {
    position: relative;
    width: 1200px;
    height: 829px;
    font-family: "Noto Sans", Arial, sans-serif;
  }
  .card {
    position: absolute;
    width: 679px;
    height: 387px;
    border-radius: 7px;
    overflow: hidden;
    background: linear-gradient(20deg, var(--blush) 0%, var(--peach) 50%, var(--butter) 100%);
  }
  .card--front { left: 123px; top: 62px; z-index: 2; }
  .card--back  { left: 398px; top: 380px; z-index: 1; }

  /* Front */
  .plume-motif {
    position: absolute;
    left: 118px;
    top: 100px;
    width: 455px;
    height: 185px;
    border-radius: 90px;
    background: radial-gradient(ellipse at center, var(--plume-light) 0%, var(--plume-warm) 55%, rgba(239, 227, 198, 0) 100%);
    opacity: 0.9;
  }
  .front-name {
    position: absolute;
    left: 0;
    right: 0;
    top: 140px;
    margin: 0;
    text-align: center;
    font-size: 66px;
    font-weight: 600;
    line-height: 1;
    color: var(--name);
  }
  .front-web {
    position: absolute;
    left: 0;
    right: 0;
    top: 228px;
    margin: 0;
    text-align: center;
    font-size: 24px;
    color: var(--web-light);
    text-shadow: 0 0 4px rgba(138, 107, 58, 0.55);
  }

  /* Back */
  .back-panel {
    position: absolute;
    left: 135px;
    top: 51px;
    width: 409px;
    height: 288px;
    border-radius: 4px;
    background: var(--panel);
  }
  .feather-photo {
    position: absolute;
    left: 160px;
    top: 55px;
    width: 380px;
    height: 332px;
    background: radial-gradient(ellipse 40% 60% at 60% 55%, rgba(255, 250, 240, 0.85) 0%, rgba(250, 240, 225, 0.4) 55%, rgba(250, 240, 225, 0) 100%);
  }
  .contact {
    position: absolute;
    left: 135px;
    top: 119px;
    width: 409px;
    margin: 0;
    text-align: center;
    font-size: 22px;
    line-height: 29.3px;
    color: var(--ink);
    font-style: normal;
  }
  .contact span { display: block; }
</style>
</head>
<body>
<div class="canvas">
  <section class="card card--front">
    <div class="plume-motif" role="img" aria-label="Decorative ornamental feather plume motif in cream and blush tones"></div>
    <h1 class="front-name">Marla Voss</h1>
    <p class="front-web">www.browsandblush.example</p>
  </section>

  <section class="card card--back">
    <div class="back-panel"></div>
    <div class="feather-photo" role="img" aria-label="Photograph of a soft white feather"></div>
    <address class="contact">
      <span class="contact__role">Makeup Artist</span>
      <span class="contact__phone">USA: +1 (415)872-6410</span>
      <span class="contact__phone">Singapore: +65 83027715</span>
      <span class="contact__email">marlavoss@browsandblush.example</span>
      <span class="contact__web">www.browsandblush.example</span>
    </address>
  </section>
</div>
</body>
</html>
```